Morvath Real Estate Marketing Brochure

We are looking for a refresh/modern design to use on our marketing brochures...the blue paint brush stroke takes up a lot of space and isn't really speaking to us. Most of the material does not need to be reproduced...we are just looking for a clean template that we can use on all of our brochure pages, and then would like help on page 11 to make these pages look more professional.
Target Market(s)
Real Estate Developers, Small Businesses looking to lease space
Industry/Entity Type
Real Estate Development
Requirements
Nice to have
- Colors complementing the Morvath Logo

```html
<!DOCTYPE html>
<html lang="en">
<head>
<meta charset="utf-8">
<title>Morvath Partners – Property Brochure</title>
<link href="https://fonts.googleapis.com/css2?family=Caladea&family=Montserrat:wght@500&display=swap" rel="stylesheet">
<style>
  :root {
    --page: #e8f0f8;
    --white: #ffffff;
    --heading-light: #8db3da;
    --ink-blue: #1a5ba8;
    --rule-blue: #1f6fc0;
    --logo-navy: #27355e;
    --photo-sky: #a9d2e8;
    --photo-brick: #a0614c;
    --plan-grey: #dcdcdc;
    --plan-blue: #7ea3cb;
  }
  * { margin: 0; padding: 0; box-sizing: border-box; }
  html, body { width: 1200px; height: 928px; overflow: hidden; background: var(--page); }
  .brochure {
    position: relative; width: 1200px; height: 928px;
    background: var(--page);
    font-family: "Caladea", Cambria, Georgia, serif;
    color: var(--ink-blue);
    overflow: hidden;
  }
  .corner { position: absolute; }
  .corner--top { left: 0; top: 0; }
  .corner--bottom { right: 0; bottom: 0; }

  .hero-photo {
    position: absolute; left: 0; top: 0; width: 600px; height: 463px;
    background: linear-gradient(160deg, var(--photo-sky) 0%, #c4a79a 50%, var(--photo-brick) 100%);
    clip-path: polygon(172px 0, 600px 0, 600px 463px, 0 463px, 0 120px);
  }

  .brand {
    position: absolute; left: 866px; top: 34px;
    display: flex; align-items: center; gap: 12px;
  }
  .brand__mark { width: 30px; height: 30px; background: var(--logo-navy); }
  .brand__name {
    font-family: "Montserrat", Arial, sans-serif; font-weight: 500;
    color: var(--logo-navy); font-size: 44px; letter-spacing: 1px; line-height: 1;
  }
  .brand__tag {
    position: absolute; right: 0; top: 50px;
    font-family: "Montserrat", Arial, sans-serif; font-weight: 500;
    color: var(--logo-navy); font-size: 15px; letter-spacing: 1.5px;
  }

  .section-title { color: var(--heading-light); font-weight: 400; line-height: 1; }

  .location { position: absolute; left: 660px; top: 144px; }
  .location .section-title { font-size: 57px; }
  .location__lines { margin-top: 4px; font-size: 36px; line-height: 43px; }
  .location__rule { width: 214px; height: 2px; background: var(--rule-blue); margin: 8px 0 4px; }
  .location__facts { font-size: 19.5px; line-height: 21.5px; }

  .floorplan-info { position: absolute; left: 53px; top: 506px; }
  .floorplan-info .section-title { font-size: 57px; }
  .floorplan-info__lines { margin-top: 10px; font-size: 36px; letter-spacing: 4px; line-height: 53px; }
  .floorplan-info__rule { width: 508px; height: 2px; background: var(--rule-blue); margin-top: 22px; }

  .contact { position: absolute; left: 53px; top: 738px; }
  .contact .section-title { font-size: 57px; }
  .contact__lines { margin-top: 4px; font-size: 26px; line-height: 28.5px; font-style: normal; }

  .plan {
    position: absolute; left: 600px; top: 463px; width: 600px; height: 465px;
    background: var(--white);
  }
  .plan__drawing {
    position: absolute; left: 36px; top: 18px; width: 524px; height: 440px;
    background: linear-gradient(180deg, var(--plan-grey) 0%, #c9d5e4 50%, var(--plan-blue) 100%);
  }
</style>
</head>
<body>
<main class="brochure">
  <div class="hero-photo" role="img" aria-label="Rendering of the renovated two-storey brick office building with awnings, street lamps and landscaping"></div>
  <svg class="corner corner--top" width="172" height="120" aria-hidden="true"><polygon points="0,0 172,0 0,120" fill="var(--page)"/></svg>

  <div class="brand">
    <span class="brand__mark"></span>
    <span class="brand__name">MORVATH</span>
    <span class="brand__tag">PARTNERS</span>
  </div>

  <section class="location">
    <h2 class="section-title">Location:</h2>
    <p class="location__lines">Aerial<br>218 North Larkin Avenue<br>Brookhaven Falls, IL 60917</p>
    <div class="location__rule"></div>
    <p class="location__facts">57,856 Gross Square Feet<br>19,222 SF Floorplates<br>Renovations Planned (2021)</p>
  </section>

  <section class="floorplan-info">
    <h2 class="section-title">First Floor Floorplan:</h2>
    <p class="floorplan-info__lines">19,222 SF Floorplate<br>Suites From 1,338 SF</p>
    <div class="floorplan-info__rule"></div>
  </section>

  <section class="contact">
    <h2 class="section-title">Contact:</h2>
    <address class="contact__lines">Daniel Reverholt<br>T: 555 - 318 - 0274<br>dreverholt@morvathpartners.com</address>
  </section>

  <div class="plan">
    <div class="plan__drawing" role="img" aria-label="First floor architectural plan showing existing open office, restrooms, stairs and available suites highlighted in blue"></div>
  </div>

  <svg class="corner corner--bottom" width="150" height="115" aria-hidden="true"><polygon points="150,0 150,115 0,115" fill="var(--page)"/></svg>
</main>
</body>
</html>
```